Quiet Harbor
How Opening the Palate Renews Rest, Vigor, and Poise Without an Operation
Creative Brief
Description: I’m seeking a talented designer to create a professional, simple, and wellness-oriented cover for my upcoming book. The book explores the hidden connection between jaw expansion, airway health, and whole-body wellness. What I’m Looking For: Clean, minimalist style (similar to Tidal by Colin Marsby and The Lumen Method by Gregory Tallisant). A design that communicates both trustworthiness and transformation — this is a serious wellness/health book, not a textbook. Imagery that subtly conveys space, breathing, and expansion (abstract or symbolic — not literal medical images). Professional typography with good spacing and balance. A design that looks credible in both print and digital formats (Amazon, bookstore, audiobook). Deliverables: Front cover design (with title, subtitle, author name). Full jacket design (front, spine, back cover with provided text). Final files in print-ready PDF + high-res PNG/JPEG + source files (AI/PSD/INDD). About the Author: Dr. Darren Okafield, DMD, is a board-certified orthodontist and dentofacial orthopedist recognized internationally for his airway-focused approach. Featured in Plain Ease, Vantage Wellbeing, and BX Magazine, he helps patients achieve healthier smiles and better breathing without unnecessary surgery.
Health
Health minded people. Men and women but maybe lean a little more toward women
Design the front and back cover. Attached is a current design but I want to go with a new title subtitle of: Title: Open Passage Subtitle: The Quiet Link Among Inhaling, Rest, and Total Vitality ... I'm also open to other titles that might convey a similar message. Here is the back of the book description: What if the cause of your fatigue, poor sleep, anxiety, or lack of focus wasn’t in your mind—but in your mouth? Hidden jaw and airway problems affect millions of adults, yet most go undiagnosed. A narrow palate, mouth breathing, or underdeveloped jaws can quietly disrupt your health, appearance, and energy every single day. In this groundbreaking book, Dr. Darren Okafield—board-certified orthodontist, dentofacial orthopedist, airway-focused clinician, and author of The Kolvex Principle—reveals how your smile, facial balance, and airway are deeply connected to whole-body health. Through real patient stories, simple science, and clear explanations of modern treatment approaches, you’ll discover: The hidden epidemic of underdeveloped jaws and how it impacts breathing, sleep, wellness, and facial harmony Why mouth breathing is more than a bad habit—it’s a health disruptor The truth about palate expanders for adults and children (and what’s important to know about them) What to expect on your treatment journey, from first consultation to long-term results How better breathing can transform not only your health—but also your confidence and overall vitality This isn’t just about teeth. It’s about unlocking the power of proper breathing, creating balance in the face, and giving your body the space it needs to thrive. If you’ve ever felt like something was “off” with your health but couldn’t find the root cause, this book offers the missing link—and a guide to lasting transformation. About the Author Dr. Darren Okafield is a board-certified orthodontist and dentofacial orthopedist and founder of TrelbyBraceClinic.example. Recognized internationally for his airway-focused approach, he helps children, teens, and adults achieve healthier smiles and better breathing without unnecessary surgery. Featured in Plain Ease, Vantage Wellbeing, and with an upcoming expert feature in BX Magazine, he is passionate about educating both consumers and professionals on the life-changing connection between orthodontics, facial development, and whole-body health.

```html
<!DOCTYPE html>
<html lang="en">
<head>
<meta charset="utf-8">
<title>Open Passage — Front Cover</title>
<link rel="stylesheet" href="https://fonts.googleapis.com/css2?family=Libre+Baskerville:wght@400;700&display=swap">
<style>
  :root {
    --stage: #e8e9e9;
    --mint-light: #d7efed;
    --mint: #b9e2df;
    --mint-deep: #9fd3cf;
    --ink: #1f4f4c;
  }
  html, body {
    margin: 0;
    padding: 0;
    width: 1200px;
    height: 901px;
    overflow: hidden;
    background: var(--stage);
  }
  .stage {
    position: relative;
    width: 1200px;
    height: 901px;
  }
  .book-cover {
    position: absolute;
    left: 390px;
    top: 115px;
    width: 440px;
    height: 670px;
    overflow: hidden;
    background: var(--mint);
    box-shadow: 0 10px 30px rgba(0, 0, 0, 0.12);
    font-family: "Libre Baskerville", Georgia, serif;
    color: var(--ink);
  }
  .cover-art {
    position: absolute;
    inset: 0;
    background:
      radial-gradient(ellipse 70% 30% at 70% 30%, rgba(255,255,255,0.45), transparent 70%),
      radial-gradient(ellipse 80% 25% at 40% 62%, rgba(255,255,255,0.35), transparent 70%),
      linear-gradient(160deg, var(--mint-light) 0%, var(--mint) 50%, var(--mint-deep) 100%);
  }
  .cover-text {
    position: absolute;
    left: 42px;
    right: 42px;
    top: 52px;
  }
  .title {
    margin: 0;
    font-weight: 700;
    font-size: 58px;
    line-height: 1.02;
    letter-spacing: 2px;
    text-transform: uppercase;
  }
  .subtitle {
    margin: 34px 0 0;
    font-weight: 400;
    font-size: 15px;
    line-height: 1.35;
    letter-spacing: 1px;
    text-transform: uppercase;
    max-width: 300px;
  }
  .byline {
    position: absolute;
    left: 42px;
    top: 470px;
    font-size: 15px;
    line-height: 1.5;
  }
  .byline-label {
    display: block;
    font-weight: 700;
  }
</style>
</head>
<body>
  <main class="stage">
    <section class="book-cover">
      <div class="cover-art" role="img" aria-label="Abstract soft flowing translucent waves in pale mint tones"></div>
      <div class="cover-text">
        <h1 class="title">Open<br>Passage</h1>
        <p class="subtitle">The Quiet Link Among Inhaling, Rest, and Total Vitality</p>
      </div>
      <p class="byline">
        <span class="byline-label">Written By:</span>
        Dr Darren Okafield, DMD
      </p>
    </section>
  </main>
</body>
</html>
```